Golden Hands Care Business Needs a New Website

Hello,
We require a website to be designed and coded. The design and coding must be high quality. Our website host has requested files be in static HTML format if possible.

The business is a mobile massage service for seniors (elderly people). The designer should emphasise that the business is a mobile service

The website will only have 4 pages.

1. Home- very simple layout and minimal information
2. Massage Services- this houses all of the information about the different services etc.
3. Contact Us-
4. ホーム (this is the Japanese symbol for 'home')- All of the information on the home page (section 1) will be translated into Japanese and uploaded to the brief for the designers to insert.

There is no requirement for an online booking, just contact information. The words 'Make a Booking' can be used and should lead customers to the 'Contact Us' page.

I have attached the business logo in multiple formats for designers to use.

I will upload more content and images to use for the website by the end of this week.

Thank you. I look forward to working with the successful candidate.

Target Market(s)

People aged 50+ years

Industry/Entity Type

Massage Therapy

Coding

Coded - Design and coding required

Number of Pages Required

4 page

Font styles to use
Sans Serif

Colors
74cabd
abd036
9ccb3b
f6faec
ffffff

Requirements
Must have
• Copyright free images and photos that we have taken. Both are important.
• Simple and inviting design.
Nice to have
• Colours of the logo incorporated.
Should not have
• This business is not a massage shop, so no images of massage shops or day salons required.
• Not too much imagery as the design needs to be simple.

```html
<!DOCTYPE html>
<html lang="en">
<head>
<meta charset="utf-8">
<title>Golden Hands Care – Mobile Massage for Seniors</title>
<link href="https://fonts.googleapis.com/css2?family=Open+Sans:ital,wght@0,400;0,600;0,700;1,400&display=swap" rel="stylesheet">
<style>
:root{
  --teal:#74cabd;
  --teal-deep:#33b5a1;
  --green:#9ccb3b;
  --green-soft:#abd036;
  --cream:#f6faec;
  --band:#eef5f4;
  --white:#ffffff;
  --ink:#222222;
  --text:#555555;
  --muted:#777777;
  --rule:#dddddd;
}
*{margin:0;padding:0;box-sizing:border-box}
html,body{width:1200px;height:2182px;overflow:hidden;background:var(--white)}
body{position:relative;font-family:"Open Sans",Arial,sans-serif;color:var(--text)}
.abs{position:absolute}
a{text-decoration:none;color:inherit}

/* header */
.topline{left:0;top:0;width:1200px;height:4px;background:var(--teal)}
.brand{display:flex;align-items:center;gap:12px;color:var(--green)}
.brand-dot{width:34px;height:34px;border-radius:50%;background:var(--green)}
.brand-name{font-size:20px;font-weight:400;letter-spacing:.5px;white-space:nowrap}
.brand-sub{font-size:9px;letter-spacing:5px;color:var(--muted);text-align:center;margin-top:2px;border-top:1px solid var(--muted);padding-top:2px}
.header-brand{left:97px;top:24px}
.contact-row{top:20px;right:95px;display:flex;gap:30px;font-size:15px;color:#444}
.contact-item{display:flex;align-items:center;gap:10px}
.ic-circle{width:26px;height:26px;border-radius:50%;border:1px solid var(--rule);display:flex;align-items:center;justify-content:center}
.nav{top:63px;left:413px;display:flex;gap:0;font-size:15px;color:#333}
.nav a{margin-right:30px}
.nav a.active{color:var(--green)}
.search{left:1088px;top:66px}

/* hero */
.hero{left:0;top:102px;width:1200px;height:430px;background:linear-gradient(100deg,#6d6a5c 0%,#8a8b74 35%,#4d6b3f 60%,#c9ccc4 100%)}
.hero-shade{left:0;top:102px;width:1200px;height:430px;background:linear-gradient(90deg,rgba(0,0,0,.35),rgba(0,0,0,0) 60%)}
.hero-title{left:98px;top:218px;font-size:52px;font-weight:700;color:var(--white);letter-spacing:.5px}
.hero-text{left:99px;top:292px;width:600px;font-size:14.5px;line-height:27px;color:var(--white)}
.btn-solid{background:var(--green);color:var(--white);font-weight:700;font-size:14px;display:flex;align-items:center;justify-content:center;gap:8px}
.hero-btn{left:99px;top:364px;width:202px;height:37px}
.dots{left:545px;top:480px;display:flex;gap:8px}
.dots span{width:24px;height:4px;background:var(--white);border-radius:2px}
.dots span.on{background:var(--green)}

/* welcome */
.sec-title{width:1200px;left:0;text-align:center;font-size:24px;font-weight:700;color:var(--ink)}
.welcome-title{top:580px}
.welcome-text{left:190px;top:628px;width:820px;text-align:center;font-size:12px;line-height:25px;color:var(--muted)}
.feature{top:708px;width:320px;text-align:center}
.feature-ring{width:192px;height:192px;margin:0 auto;border-radius:50%;border:1px solid var(--teal);display:flex;align-items:center;justify-content:center}
.feature-ring-inner{width:178px;height:178px;border-radius:50%;border:4px solid var(--teal);display:flex;align-items:center;justify-content:center}
.feature h3{margin-top:24px;font-size:17px;font-weight:400;color:var(--ink)}
.feature p{margin-top:12px;font-size:12px;line-height:22px;color:var(--muted)}
.btn-outline{display:inline-block;margin-top:17px;width:125px;height:29px;line-height:27px;border:1px solid #999;color:var(--green);font-size:12px;font-weight:600}

/* what we do */
.what-band{left:0;top:1095px;width:1200px;height:387px;background:var(--band)}
.what-title{left:99px;top:1142px;font-size:24px;font-weight:700;color:var(--ink)}
.what-text{left:99px;top:1193px;width:460px;font-size:12px;line-height:25px;color:var(--muted)}
.what-text p+p{margin-top:25px}
.what-btn{left:99px;top:1393px;width:129px;height:34px;font-size:12px;box-shadow:0 1px 3px rgba(0,0,0,.2)}
.video{left:607px;top:1145px;width:494px;height:286px;border:4px solid var(--white);box-shadow:0 0 3px rgba(0,0,0,.2);background:linear-gradient(110deg,#7d7e78 0%,#9aa19a 30%,#486e3a 60%,#5f8a3f 100%)}
.play{left:823px;top:1258px}

/* testimonials */
.testi-title{top:1530px}
.avatar{left:106px;top:1583px;width:128px;height:128px;border-radius:50%;border:3px solid #e6e6e6;background:radial-gradient(circle at 50% 40%,#e9dcd2,#b7a89b)}
.testi-rule{left:269px;top:1583px;width:1px;height:127px;background:var(--rule)}
.quote{left:301px;top:1587px;width:800px;font-size:14px;font-style:italic;line-height:27px;color:var(--muted)}
.quote-name{left:301px;top:1683px;font-size:17px;color:var(--green)}
.arrow{top:1632px}

/* cta band */
.cta{top:1763px;height:84px;display:flex;align-items:center;gap:16px;color:var(--white);padding-left:95px}
.cta h4{font-size:17px;font-weight:600;letter-spacing:.3px}
.cta p{font-size:12px;margin-top:4px}
.cta-1{left:0;width:403px;background:var(--teal-deep)}
.cta-2{left:403px;width:394px;background:var(--green);padding-left:78px}
.cta-3{left:797px;width:403px;background:var(--teal-deep);padding-left:55px}

/* footer */
.footer-brand{left:90px;top:1945px;width:280px;display:flex;flex-direction:column;align-items:center;color:var(--green)}
.footer-brand .brand-dot{width:60px;height:60px;margin-bottom:14px}
.footer-brand .brand-name{font-size:24px}
.footer-brand .brand-sub{width:270px}
.f-title{top:1895px;font-size:17px;color:var(--ink)}
.f-links{left:430px;top:1935px;font-size:12px;line-height:19px;color:#444}
.f-news{left:609px;top:1937px;width:250px;font-size:12px;line-height:20px;color:#555}
.f-input{left:609px;top:1990px;width:255px;height:32px;border-bottom:1px solid #bbb;font-size:11px;color:#aaa;padding:10px 14px}
.f-btn{left:609px;top:2037px;width:93px;height:32px;border:1px solid #999;color:var(--green);font-size:11px;font-weight:600;display:flex;align-items:center;justify-content:center}
.f-contact{left:919px;font-size:12px;line-height:21px;color:#444;display:flex;gap:14px}
.f-rule{left:99px;top:2109px;width:1002px;height:1px;background:var(--rule)}
.copy{left:99px;top:2136px;font-size:12px;color:#444}
.socials{left:975px;top:2127px;display:flex;gap:8px}
.socials span{width:26px;height:26px;border-radius:50%;border:1px solid var(--green)}
</style>
</head>
<body>

<header>
  <div class="abs topline"></div>
  <a class="abs brand header-brand" href="#">
    <span class="brand-dot"></span>
    <span>
      <span class="brand-name">GOLDEN HANDS CARE</span>
      <span class="brand-sub" style="display:block">AUSTRALIA</span>
    </span>
  </a>
  <div class="abs contact-row">
    <span class="contact-item">
      <span class="ic-circle"><svg width="13" height="13" viewBox="0 0 24 24"><path fill="#9ccb3b" d="M6.6 10.8a15.1 15.1 0 0 0 6.6 6.6l2.2-2.2c.3-.3.7-.4 1-.2 1.1.4 2.3.6 3.6.6.6 0 1 .4 1 1V20c0 .6-.4 1-1 1A17 17 0 0 1 3 4c0-.6.4-1 1-1h3.5c.6 0 1 .4 1 1 0 1.3.2 2.5.6 3.6.1.3 0 .7-.2 1z"/></svg></span>
      0400 118 226
    </span>
    <span class="contact-item">
      <span class="ic-circle"><svg width="13" height="11" viewBox="0 0 24 18"><path fill="#9ccb3b" d="M0 0h24v18H0z"/><path fill="none" stroke="#fff" stroke-width="2" d="M1 1l11 9 11-9"/></svg></span>
      hello@goldenhandscare.example
    </span>
  </div>
  <nav class="abs nav">
    <a class="active" href="#">Home</a>
    <a href="#">About us</a>
    <a href="#">Home Care Services</a>
    <a href="#">Careers</a>
    <a href="#">Resources</a>
    <a href="#">Blog</a>
    <a href="#">Contact Us</a>
  </nav>
  <svg class="abs search" width="15" height="15" viewBox="0 0 16 16"><circle cx="6.5" cy="6.5" r="5" fill="none" stroke="#222" stroke-width="2.2"/><path d="M10 10l5 5" stroke="#222" stroke-width="2.5"/></svg>
</header>

<section>
  <div class="abs hero" role="img" aria-label="Photo of a therapist giving a mobile massage to a senior client on a garden lawn"></div>
  <div class="abs hero-shade"></div>
  <h1 class="abs hero-title">GOLDEN HANDS CARE</h1>
  <p class="abs hero-text">At vero eos et accusamus et iusto odio dignissimos ducimus qui blanditiis pr aesent ium voluptatum deleniti atque corrupti accusa culpa quiquos.</p>
  <a class="abs btn-solid hero-btn" href="#">
    <svg width="15" height="15" viewBox="0 0 16 16"><rect x="1" y="2.5" width="14" height="12.5" fill="none" stroke="#fff" stroke-width="1.6"/><path d="M1 6h14M4.5 0.5v4M11.5 0.5v4" stroke="#fff" stroke-width="1.6"/></svg>
    MAKE A BOOKING
  </a>
  <div class="abs dots"><span class="on"></span><span></span><span></span><span></span></div>
</section>

<section>
  <h2 class="abs sec-title welcome-title">WELCOME TO GOLDEN HANDS CARE</h2>
  <p class="abs welcome-text">At vero eos et accusamus et iusto odio dignissimos ducimus qui blanditiis praesentium voluptatum deleniti atque corrupti quos dolores et quas molestias excepturi sint occae sunt in culpa qui officia deserunt mollitia est laborum et dolorumlis est et expedita distinctio.</p>

  <div class="abs feature" style="left:80px">
    <div class="feature-ring"><div class="feature-ring-inner">
      <svg width="66" height="58" viewBox="0 0 24 21"><path fill="#9ccb3b" d="M12 21L2.3 11.6A6 6 0 0 1 12 3.3a6 6 0 0 1 9.7 8.3z"/></svg>
    </div></div>
    <h3>Home Care Services</h3>
    <p>At vero eos et accusamus et iusto odio dignissimos<br>ducimus qui blanditiis praesentium volupt</p>
    <a class="btn-outline" href="#">GET STARTED</a>
  </div>

  <div class="abs feature" style="left:440px">
    <div class="feature-ring"><div class="feature-ring-inner">
      <svg width="66" height="60" viewBox="0 0 24 22"><path fill="none" stroke="#9ccb3b" stroke-width="2" d="M8 5V2h8v3"/><rect x="0" y="5" width="24" height="17" rx="2" fill="#9ccb3b"/><path d="M5 5v17M19 5v17" stroke="#fff" stroke-width="1.3"/></svg>
    </div></div>
    <h3>Massage Care Careers</h3>
    <p>At vero eos et accusamus et iusto odio dignissimos<br>ducimus qui blanditiis praesentium volupt</p>
    <a class="btn-outline" href="#">FIND JOBS</a>
  </div>

  <div class="abs feature" style="left:798px">
    <div class="feature-ring"><div class="feature-ring-inner">
      <svg width="72" height="64" viewBox="0 0 28 25"><circle cx="6" cy="6" r="3.5" fill="#9ccb3b"/><circle cx="22" cy="6" r="3.5" fill="#9ccb3b"/><circle cx="14" cy="8" r="4.5" fill="#9ccb3b"/><path fill="#9ccb3b" d="M0 16c0-4 2.5-6 6-6s4 1 4 1-3 2-3 7H0zM28 16c0-4-2.5-6-6-6s-4 1-4 1 3 2 3 7h7zM6 25c0-7 3-10 8-10s8 3 8 10z"/></svg>
    </div></div>
    <h3>Become a Care Giver</h3>
    <p>At vero eos et accusamus et iusto odio dignissimos<br>ducimus qui blanditiis praesentium volupt</p>
    <a class="btn-outline" href="#">JOIN US</a>
  </div>
</section>

<section>
  <div class="abs what-band"></div>
  <h2 class="abs what-title">WHAT WE DO</h2>
  <div class="abs what-text">
    <p>At vero eos et accusamus et iusto odio dignissimos ducimus qui blanditiis prasent ium voluptatum deleniti atque corrupti quo.</p>
    <p>Dolores et quas molestias excepturi sint occaecati cupiditate non provident similiq ue sunt in culpa qui officia deserunt mollitia animi, id est laborum et dolorum fug t harum quidem rerum facilis est et expedita voluptas assumenda est, omnis dolorr epellend poribus autem quibusdam et aut officiis.</p>
  </div>
  <a class="abs btn-solid what-btn" href="#">READ MORE &gt;&gt;</a>
  <div class="abs video" role="img" aria-label="Video still of a therapist massaging a senior client's back outdoors"></div>
  <svg class="abs play" width="62" height="62" viewBox="0 0 62 62"><circle cx="31" cy="31" r="29" fill="rgba(0,0,0,.6)" stroke="#fff" stroke-width="2"/><path d="M24 18l20 13-20 13z" fill="#fff"/></svg>
</section>

<section>
  <h2 class="abs sec-title testi-title">CLIENT TESTIMONIALS</h2>
  <svg class="abs arrow" style="left:34px" width="18" height="30" viewBox="0 0 18 30"><path d="M15 2L3 15l12 13" fill="none" stroke="#bbb" stroke-width="2.5"/></svg>
  <svg class="abs arrow" style="left:1145px" width="18" height="30" viewBox="0 0 18 30"><path d="M3 2l12 13L3 28" fill="none" stroke="#bbb" stroke-width="2.5"/></svg>
  <div class="abs avatar" role="img" aria-label="Portrait photo of the client"></div>
  <div class="abs testi-rule"></div>
  <p class="abs quote">Nam libero tempore, cum soluta nobis est eligendi optio cumque nihil impedit quo minus id quod maxime placeat facere possimus omnis voluptas assumenda est, omnis dolor repellendus. Temporibus autem quibusdam et aut officiis debitis aut rerum necessitati bus saepe eveniet ut et voluptates repudiandae sint et molestiae</p>
  <p class="abs quote-name">- Margaret Ellison</p>
</section>

<section>
  <a class="abs cta cta-1" href="#">
    <svg width="50" height="40" viewBox="0 0 50 40"><ellipse cx="20" cy="15" rx="18" ry="12" fill="none" stroke="#fff" stroke-width="3"/><path d="M8 24l-4 9 11-6" fill="none" stroke="#fff" stroke-width="3"/><path d="M40 12c6 2 9 6 9 10 0 3-2 6-5 8l3 7-10-4" fill="none" stroke="#fff" stroke-width="3"/></svg>
    <div><h4>QUICK ENQUIRY</h4><p>Nam libero tempore um solutnob</p></div>
  </a>
  <a class="abs cta cta-2" href="#">
    <svg width="40" height="40" viewBox="0 0 40 40"><rect x="2" y="6" width="36" height="32" fill="none" stroke="#fff" stroke-width="3"/><path d="M2 14h36M10 1v9M30 1v9M10 20v14M18 20v14M26 20v14M6 24h28M6 30h28" stroke="#fff" stroke-width="2.5"/></svg>
    <div><h4>MAKE A BOOKING</h4><p>Nam libero tempore um solutnob</p></div>
  </a>
  <a class="abs cta cta-3" href="#">
    <svg width="50" height="36" viewBox="0 0 50 36"><rect x="8" y="2" width="40" height="32" fill="none" stroke="#fff" stroke-width="3"/><path d="M8 8H2v24a2 2 0 0 0 4 0V8" fill="none" stroke="#fff" stroke-width="3"/><rect x="14" y="8" width="14" height="10" fill="none" stroke="#fff" stroke-width="2.5"/><path d="M32 10h11M32 16h11M14 23h29M14 28h29" stroke="#fff" stroke-width="2.5"/></svg>
    <div><h4>UPCOMING NEWS</h4><p>Nam libero tempore um solutnob</p></div>
  </a>
</section>

<footer>
  <div class="abs footer-brand">
    <span class="brand-dot"></span>
    <span class="brand-name">GOLDEN HANDS CARE</span>
    <span class="brand-sub">AUSTRALIA</span>
  </div>

  <h4 class="abs f-title" style="left:430px">Information</h4>
  <ul class="abs f-links" style="list-style:none">
    <li>Home</li><li>About us</li><li>Home Care Services</li><li>Careers</li><li>Resources</li><li>Blog</li><li>Contact Us</li>
  </ul>

  <h4 class="abs f-title" style="left:609px">Newsletter Subscription</h4>
  <p class="abs f-news">Register your Email Address to get Information about us</p>
  <div class="abs f-input">Email Address</div>
  <a class="abs f-btn" href="#">SUBSCRIBE</a>

  <h4 class="abs f-title" style="left:919px">Contact Us</h4>
  <div class="abs f-contact" style="top:1936px">
    <svg width="11" height="15" viewBox="0 0 12 16" style="margin-top:3px"><path fill="#9ccb3b" d="M6 0a6 6 0 0 0-6 6c0 4.5 6 10 6 10s6-5.5 6-10a6 6 0 0 0-6-6zm0 8.5A2.5 2.5 0 1 1 6 3.5a2.5 2.5 0 0 1 0 5z"/></svg>
    <span>12 Willow Lane,<br>4000 Brisbane - Australia</span>
  </div>
  <div class="abs f-contact" style="top:2006px">
    <svg width="13" height="13" viewBox="0 0 24 24" style="margin-top:3px"><path fill="#9ccb3b" d="M6.6 10.8a15.1 15.1 0 0 0 6.6 6.6l2.2-2.2c.3-.3.7-.4 1-.2 1.1.4 2.3.6 3.6.6.6 0 1 .4 1 1V20c0 .6-.4 1-1 1A17 17 0 0 1 3 4c0-.6.4-1 1-1h3.5c.6 0 1 .4 1 1 0 1.3.2 2.5.6 3.6.1.3 0 .7-.2 1z"/></svg>
    <span>0400 118 226</span>
  </div>
  <div class="abs f-contact" style="top:2050px">
    <svg width="14" height="11" viewBox="0 0 24 18" style="margin-top:5px"><path fill="#9ccb3b" d="M0 0h24v18H0z"/><path fill="none" stroke="#fff" stroke-width="2" d="M1 1l11 9 11-9"/></svg>
    <span>hello@goldenhandscare.example</span>
  </div>

  <div class="abs f-rule"></div>
  <p class="abs copy">Copyrights © 2016, Golden Hands Care. All rights reserved.</p>
  <div class="abs socials" aria-label="Social links"><span></span><span></span><span></span><span></span></div>
</footer>

</body>
</html>
```